The Verity (wine label)

We are creating a new wine label for our vineyard in Tasmania, Australia.
This wine is dedicated to a very special person and needs to reflect elegance, beauty and longevity. We are looking for a wine label that incorporates the artwork on the attached photo (serpent tattoo).
We are calling the wine "The Verity" and it is a Pinot Noir (red wine). It is a light bodied but elegant wine, which reflects the person that it is named after.
The wine will be a 2024 Vintage Pinot Noir.

```html
<!DOCTYPE html>
<html lang="en">
<head>
<meta charset="UTF-8">
<title>The Verity – Pinot Noir 2024 Label</title>
<link href="https://fonts.googleapis.com/css2?family=Playfair+Display:wght@700;900&family=Montserrat:wght@600;700&display=swap" rel="stylesheet">
<style>
  :root {
    --backdrop: #cbcbcb;
    --paper: #e8e5e0;
    --ink: #111111;
    --gold-deep: #c98a1e;
    --gold-mid: #e6a93a;
    --gold-light: #f3dc9c;
    --gold-pale: #f6ecd0;
    --artwork-centre: #d8d1c3;
  }
  * { margin: 0; padding: 0; box-sizing: border-box; }
  html, body {
    width: 1200px;
    height: 1117px;
    overflow: hidden;
    background: var(--backdrop);
  }
  .label {
    position: absolute;
    left: 240px;
    top: 140px;
    width: 720px;
    height: 838px;
    background: var(--paper);
    color: var(--ink);
  }
  .brand-name {
    position: absolute;
    top: 112px;
    left: 0;
    width: 100%;
    text-align: center;
    font-family: "Playfair Display", serif;
    font-weight: 900;
    font-size: 118px;
    line-height: 1;
    letter-spacing: -1px;
  }
  .origin-line {
    position: absolute;
    top: 234px;
    left: 110px;
    right: 110px;
    display: flex;
    justify-content: space-between;
    font-family: "Montserrat", sans-serif;
    font-weight: 700;
    font-size: 15px;
    letter-spacing: 0.5px;
  }
  .serpent-artwork {
    position: absolute;
    top: 262px;
    left: 138px;
    width: 444px;
    height: 302px;
    border-radius: 222px 222px 0 0;
    background:
      radial-gradient(ellipse 62% 78% at 50% 100%, var(--artwork-centre) 0%, var(--artwork-centre) 45%, var(--gold-light) 78%, var(--gold-mid) 100%);
  }
  .varietal {
    position: absolute;
    top: 560px;
    left: 0;
    width: 100%;
    text-align: center;
    font-family: "Playfair Display", serif;
    font-weight: 900;
    font-size: 80px;
    line-height: 1;
    letter-spacing: -1px;
  }
  .vintage-rule {
    position: absolute;
    top: 642px;
    left: 120px;
    right: 120px;
    display: flex;
    align-items: center;
    gap: 10px;
  }
  .vintage-rule svg { flex: 1; height: 8px; }
  .vintage-rule span {
    font-family: "Playfair Display", serif;
    font-weight: 700;
    font-size: 22px;
    letter-spacing: 10px;
    margin-right: -10px;
    line-height: 1;
  }
  .year {
    position: absolute;
    top: 702px;
    left: 0;
    width: 100%;
    text-align: center;
    font-family: "Montserrat", sans-serif;
    font-weight: 700;
    font-size: 34px;
    letter-spacing: 5px;
  }
  .gold-band {
    position: absolute;
    left: 0;
    bottom: 0;
    width: 100%;
    height: 42px;
    background: linear-gradient(90deg, var(--gold-deep), var(--gold-light) 30%, var(--gold-mid) 55%, var(--gold-light) 75%, var(--gold-mid));
  }
</style>
</head>
<body>
  <div class="label">
    <h1 class="brand-name">VERITY</h1>
    <div class="origin-line">
      <span>VINEYARD IN TASMANIA</span>
      <span>AUSTRALIA</span>
    </div>
    <div class="serpent-artwork" role="img" aria-label="Tattoo-style black serpent coiled in front of a gold ornamental arch"></div>
    <h2 class="varietal">PINOT NOIR</h2>
    <div class="vintage-rule">
      <svg viewBox="0 0 100 8" preserveAspectRatio="none"><polygon points="0,4 100,1 100,7" fill="var(--ink)"/></svg>
      <span>VINTAGE</span>
      <svg viewBox="0 0 100 8" preserveAspectRatio="none"><polygon points="0,1 100,4 0,7" fill="var(--ink)"/></svg>
    </div>
    <p class="year">2024</p>
    <div class="gold-band"></div>
  </div>
</body>
</html>
```